I need a logo design for a new company based in Tucson called "Mindtrainer Lou Varga". I am a psychotherapist that specializes in clinical psychology with athletes and performers. The final design should incorporate the psychology symbol as a watermark. The logo should convey movement and fluidity. "Mindtrainer" is a bit of a play on words combining psychology (head) with sports (coach). Other design interests include mid-century, Gustav Orrin Pell. I will want to use the logo for business cards, letterhead and marketing brochures. I will put together a website at a later date. I am attaching a file with some pertinent information for the business card. Thank you.
Lou Varga
mindtrainerlouvarga@quellmail.net
Updates

Thank you all for the submissions so far.  I have submitted an additional file with a draft of a new design idea.  Since "mindtrainer" is a bit of a play on words, I would like to see something with the two "H's" look something like quotation marks.  If the psychology logo is to be included at all, it needs to be less prominent.     Thank you all.  Lou                               

Target Market(s)

1) Adolescent and adult athletes and performers who are looking to increase their level of performance (Sport and Performance Psychology)
2) Adult psychotherapy patients (Clinical psychology)

Industry/Entity Type

Marketing

Colors

Designer to choose colors to be used in the design.

Requirements
Must have
• 1) Since "mindtrainer" is a bit of a play on words, The "H's" need to be in a font that looks somewhat like quotation marks.

Nice to have
• Logo on one side. All other info on the backside?

```html
<!DOCTYPE html>
<html lang="en">
<head>
<meta charset="utf-8">
<title>Mindtrainer Lou Varga – Business Card</title>
<link href="https://fonts.googleapis.com/css2?family=Alegreya:wght@500&family=Lato:wght@400;700&display=swap" rel="stylesheet">
<style>
  :root {
    --backdrop: #dcdcdc;
    --card: #555557;
    --accent: #7dbdb2;
    --field: #ffffff;
    --serif: "Alegreya", Georgia, serif;
    --sans: "Lato", Arial, sans-serif;
  }
  * { box-sizing: border-box; margin: 0; padding: 0; }
  html, body { width: 1200px; height: 1000px; overflow: hidden; }
  body {
    background: var(--backdrop);
    position: relative;
    color: var(--accent);
  }
  .card {
    position: absolute;
    left: 250px;
    width: 700px;
    height: 400px;
    background: var(--card);
    border-radius: 16px;
  }
  .card--front { top: 60px; }
  .card--back { top: 540px; }

  .brand {
    position: absolute;
    left: 0; right: 0; top: 120px;
    text-align: center;
  }
  .brand__name {
    font-family: var(--sans);
    font-weight: 700;
    font-size: 92px;
    letter-spacing: 2px;
    line-height: 1;
  }
  .brand__tagline {
    margin-top: 18px;
    font-family: var(--sans);
    font-weight: 400;
    font-size: 27px;
    letter-spacing: 3px;
    text-transform: uppercase;
  }

  .contact {
    position: absolute;
    left: 0; right: 0; top: 34px;
    text-align: center;
  }
  .contact__name {
    font-family: var(--serif);
    font-weight: 500;
    font-size: 44px;
    line-height: 1.05;
  }
  .contact__role {
    font-family: var(--sans);
    font-size: 19px;
    margin-bottom: 26px;
  }
  .contact__line {
    font-family: var(--sans);
    font-size: 21px;
    line-height: 1.3;
  }
  .appointment {
    position: absolute;
    left: 0; right: 0; top: 262px;
    text-align: center;
    font-family: var(--serif);
    font-size: 23px;
    letter-spacing: 1px;
    text-transform: uppercase;
  }
  .appointment__fields {
    position: absolute;
    left: 0; right: 0; top: 318px;
    display: flex;
    justify-content: center;
    gap: 56px;
    font-family: var(--sans);
    font-size: 22px;
  }
  .field { display: flex; align-items: center; gap: 14px; }
  .field__box {
    width: 210px; height: 40px;
    background: var(--field);
  }
</style>
</head>
<body>
  <section class="card card--front">
    <div class="brand">
      <div class="brand__name">Mindtrainer</div>
      <div class="brand__tagline">Clinical &amp; Performance Psychology</div>
    </div>
  </section>

  <section class="card card--back">
    <div class="contact">
      <h1 class="contact__name">Louis H. Varga, MA, LLC</h1>
      <p class="contact__role">Licensed Professional Counselor</p>
      <p class="contact__line">Fax: 520.555.0147</p>
      <p class="contact__line">Mobile: 520.555.0192</p>
      <p class="contact__line">Email: mindtrainerlouvarga@quellmail.net</p>
      <p class="contact__line">Address: 4410 East Calder #210 Tucson, AZ 85716</p>
    </div>
    <div class="appointment">Appointment</div>
    <div class="appointment__fields">
      <div class="field"><span>Date:</span><span class="field__box"></span></div>
      <div class="field"><span>Time:</span><span class="field__box"></span></div>
    </div>
  </section>
</body>
</html>
```